TriVex Business Card Design - double sided -plumbing local plumbing company

We have a Plumbing company where the design was create through Sketch Hive. We would now like a business card designed as well. We want it to be in the colour version of the logo.

Details below for the card.

Phone Number: 0438 615 247
Email: info@trivexplumbing.example.au
Website: https://trivexplumbing.example.au
We really want a sophisticated design that stand out from the other- informative and timeless.

Target Market(s)

local Canberra market

Industry/Entity Type

Plumbing, gas fitting, hot water

Contact Information for Business Card

Phone number, email, logo and "Supplying all your heating, cooling and hot water needs"

Requirements
Must have
• bust be colourful, must also be though about it being printed on a magnet. must Vex with the logo - I dont want the logo and information chucked onto a white canvas I would prefer it to be smooth and look purposeful

```html
<!DOCTYPE html>
<html lang="en">
<head>
<meta charset="utf-8">
<title>TriVex Business Card – Front and Back</title>
<link rel="stylesheet" href="https://fonts.googleapis.com/css2?family=Poppins:wght@400;500;700&display=swap">
<style>
  :root {
    --page-bg: #f1f1f1;
    --card-white: #ffffff;
    --brand-blue: #00aeef;
    --brand-orange: #f5ae45;
    --ink: #111111;
    --text-on-colour: #ffffff;
  }
  * { box-sizing: border-box; margin: 0; padding: 0; }
  html, body {
    width: 1121px;
    height: 1200px;
    overflow: hidden;
    background: var(--page-bg);
    font-family: "Poppins", Arial, sans-serif;
  }
  .sheet {
    position: relative;
    width: 1121px;
    height: 1200px;
  }
  .card {
    position: absolute;
    left: 180px;
    width: 760px;
    height: 434px;
    overflow: hidden;
    box-shadow: 0 6px 22px rgba(0, 0, 0, 0.12);
  }
  .card--front { top: 128px; background: var(--card-white); }
  .card--back  { top: 638px; background: var(--brand-blue); }

  /* Front */
  .wordmark {
    position: absolute;
    font-weight: 700;
    letter-spacing: 4px;
    line-height: 1;
    text-transform: uppercase;
  }
  .card--front .wordmark {
    top: 70px;
    left: 0;
    width: 100%;
    text-align: center;
    font-size: 104px;
    color: var(--brand-blue);
  }
  .tagline-pill {
    position: absolute;
    top: 185px;
    left: 130px;
    width: 500px;
    height: 98px;
    border-radius: 14px;
    background: linear-gradient(90deg, var(--brand-orange) 0%, var(--brand-orange) 30%, var(--brand-blue) 100%);
    display: flex;
    align-items: center;
    justify-content: center;
    text-align: center;
    color: var(--text-on-colour);
    font-size: 25px;
    font-weight: 400;
    line-height: 1.28;
  }
  .divider {
    position: absolute;
    top: 331px;
    left: 0;
    width: 100%;
    height: 3px;
    background: var(--ink);
  }
  .contact-line {
    position: absolute;
    top: 350px;
    left: 0;
    width: 100%;
    text-align: center;
    font-size: 24px;
    font-weight: 500;
    color: var(--ink);
    white-space: nowrap;
  }
  .contact-line .sep { margin: 0 12px; }

  /* Back */
  .drop-artwork {
    position: absolute;
    top: 0;
    left: 0;
    width: 440px;
    height: 100%;
    background: linear-gradient(90deg, #c9b07a 0%, var(--brand-orange) 45%, #8fb3a0 75%, var(--brand-blue) 100%);
  }
  .card--back .wordmark {
    top: 176px;
    left: 250px;
    width: 440px;
    text-align: center;
    font-size: 80px;
    color: var(--text-on-colour);
  }
</style>
</head>
<body>
  <main class="sheet">
    <section class="card card--front" aria-label="Business card front">
      <h1 class="wordmark">TriVex</h1>
      <p class="tagline-pill">Supplying all your Heating,<br>Cooling and Hot Water Needs</p>
      <div class="divider"></div>
      <p class="contact-line">Phone: 0438 615 247<span class="sep">|</span>Email: info@trivexplumbing.example.au</p>
    </section>

    <section class="card card--back" aria-label="Business card back">
      <div class="drop-artwork" role="img" aria-label="Overlapping water-drop artwork in orange-to-blue gradient"></div>
      <p class="wordmark">TriVex</p>
    </section>
  </main>
</body>
</html>
```